A modern and fresh looking church website

St Maren’s is looking for a new site design for their church. The church is a part of a group of the ‘Calverin Church’ Australia and needs to kind of tie into their branding within reason.
This means, we would need to use the logo colours (Blue, Gold, Red) throughout the website and the design needs to be fresh, modern, clean, and mobile-friendly. The front page must have the following as features:
• Sermons (Podcasts and Videos)
• Events
• Venue Hire (Weddings)
The website will be mainly information-based and will have a few forms. From our recent engagement with the church, I did draft up a mock-up design for them and even it looks better than their current site, it’s not giving a ‘stand out impression’ and has that out of date look.
The inner pages will be based off the front-page design so we will take care of that, we are just looking for a front-page design that is unique and has the wow factor.
The website will be coded by our in-house development team and will be coded in a WordPress format using Elementor pro.
We are looking for a couple of designers to design 1-3 mock-ups by taking our current draft and putting their spin to it.
Hi,
Due to Christmas and the client was on leave, the design selection has been delayed. It was not ideal as I knew this would happen.
I made contact with the client and just been told that the client is leaving the church and a handover is happening for the new staff member. The new staff member will present all designs to the board for selection. This is due to be completed by the first week of February 2021.
We thanks for your patients as this was not expected and we seeing if we can hurry this process up.

```html
<!DOCTYPE html>
<html lang="en">
<head>
<meta charset="utf-8">
<title>St Maren’s — Calverin Church Perth</title>
<link href="https://fonts.googleapis.com/css2?family=Lora:wght@400;700&family=Rubik:wght@400;500;700;800&display=swap" rel="stylesheet">
<style>
:root{
  --blue:#0a55a8;
  --blue-dark:#073f80;
  --red:#e3231f;
  --gold:#f29d38;
  --orange:#ff5a00;
  --ink:#222;
  --panel:#232425;
  --paper:#f6f6f8;
}
*{box-sizing:border-box;margin:0;padding:0}
html,body{width:1200px;height:2983px;overflow:hidden}
body{position:relative;font-family:"Lora",serif;color:var(--ink);background:#fff}
.abs{position:absolute}
a{color:inherit;text-decoration:none}

/* top bar */
.topbar{left:0;top:0;width:1200px;height:35px;background:var(--blue);color:#fff;font-size:12px;z-index:3}
.topbar .addr{left:94px;top:9px;display:flex;gap:10px;align-items:center}
.topbar .social{right:100px;top:0;display:flex;height:35px}
.topbar .social span{width:52px;height:35px;border-left:1px solid rgba(255,255,255,.3);display:flex;align-items:center;justify-content:center}
.topbar .social i{width:12px;height:12px;background:#fff;border-radius:3px;display:block}

/* header */
.brand{left:93px;top:50px;display:flex;align-items:center;gap:10px}
.brand .dot{width:48px;height:48px;border-radius:50%;background:var(--blue)}
.brand .name{font-family:"Rubik",sans-serif;font-weight:700;color:var(--blue);font-size:30px;line-height:1}
.brand .sub{font-family:"Rubik",sans-serif;font-weight:700;color:var(--blue);font-size:12px;letter-spacing:.5px;margin-top:4px}
.service{left:968px;top:48px;font-size:12px;color:var(--gold);line-height:15px}
.service b{font-family:"Rubik",sans-serif;color:var(--blue);font-size:13px;text-decoration:underline;display:block;margin-bottom:6px}

/* nav */
.nav{left:87px;top:120px;width:1027px;height:63px;z-index:3}
.nav svg{position:absolute;left:0;top:0}
.nav ul{position:absolute;left:82px;top:0;height:51px;list-style:none;display:flex;font-weight:700;font-size:14px;color:#fff}
.nav li{padding:0 27px;line-height:51px}
.nav li.active{background:var(--red)}

/* hero */
.hero{left:0;top:159px;width:1200px;height:557px;background:linear-gradient(180deg,#8f8a86 0%,#c9c4bd 40%,#d8d2c8 65%,#8a5e3c 100%)}
.hero-txt{left:0;top:272px;width:1200px;text-align:center}
.hero-txt h1{font-family:"Lora",serif;font-weight:700;font-size:64px;line-height:62px;color:#111}
.hero-txt h1 em{font-style:normal;color:var(--red)}
.hero-txt p{font-family:"Rubik",sans-serif;font-size:18px;color:#333;margin-top:34px;letter-spacing:.5px}
.btn-touch{left:514px;top:488px;width:172px;height:54px;background:var(--red);border-radius:6px;color:#fff;font-family:"Rubik",sans-serif;font-weight:700;font-size:13px;display:flex;align-items:center;justify-content:center;box-shadow:0 4px 0 #b01510}
.notch{left:575px;top:714px}

/* about */
.about{left:0;top:716px;width:1200px;height:728px;background:linear-gradient(160deg,#fff 0%,var(--paper) 100%)}
.notice{left:154px;top:760px;width:891px;height:48px;background:#f7eaec;border:1px solid #ecdadd;border-radius:4px}
.notice .ico{position:absolute;left:0;top:0;width:52px;height:46px;border-right:1px solid #e0cdd1;display:flex;align-items:center;justify-content:center}
.notice h4{position:absolute;left:74px;top:8px;font-family:"Rubik",sans-serif;font-size:13px;font-weight:500}
.notice p{position:absolute;left:73px;top:28px;font-size:10px;color:#333}
.h2{font-family:"Rubik",sans-serif;font-weight:700;font-size:21px;text-align:center}
.h2::after{content:"";display:block;width:222px;height:1px;background:var(--blue);margin:14px auto 0}
.about-copy{left:145px;top:1003px;width:470px;font-size:14px;line-height:22px;color:#333}
.about-copy p{margin-bottom:21px}
.about-copy b{color:var(--red)}
.about-art{left:695px;top:938px;width:420px;height:372px;border-radius:18px;background:linear-gradient(135deg,#c9d6f3 0%,#e9b27a 55%,#a34a3a 100%)}

/* services */
.services{left:0;top:1444px;width:1200px;height:558px;background:var(--blue)}
.services .h2{color:#fff}
.services .h2::after{background:#fff}
.card{width:351px;height:287px;background:#fff;padding:8px}
.card .pic{width:100%;height:271px;position:relative}
.card .label{position:absolute;left:0;bottom:0;width:100%;height:50px;background:rgba(242,157,56,.85);color:var(--blue);font-family:"Rubik",sans-serif;font-weight:700;font-size:15px;display:flex;align-items:center;justify-content:center}

/* contact */
.contact{left:0;top:2002px;width:1200px;height:557px;background:radial-gradient(ellipse at 60% 45%,#e8ecef 0%,#b4bcc4 55%,#8c98a3 100%)}
.ribbon{left:93px;top:2059px}
.panel{left:129px;top:2098px;width:462px;height:380px;background:var(--panel);color:#fff}
.row{position:absolute;left:56px;width:272px;height:46px;border-bottom:1px solid #888;display:flex;align-items:center;gap:14px;font-size:17px;line-height:20px}
.row .c{width:40px;height:40px;border-radius:50%;border:1px solid #2a4a7a;display:flex;align-items:center;justify-content:center;flex:none;margin-left:-2px}
.cta{left:129px;top:2478px;width:462px;height:47px;background:var(--orange);color:#fff;font-family:"Rubik",sans-serif;font-weight:700;font-size:15px;display:flex;align-items:center;justify-content:center}
.map{left:695px;top:2113px;width:448px;height:315px;border:4px solid var(--blue);background:linear-gradient(135deg,#eef0f3,#e2e6ea)}

/* footer */
.footer{left:0;top:2559px;width:1200px;height:342px;background:var(--blue);color:#fff}
.footer h5{position:absolute;top:56px;font-family:"Rubik",sans-serif;font-weight:700;font-size:17px}
.footer h5::after{content:"";display:block;width:78px;height:1px;background:var(--gold);margin-top:10px}
.f-brand{left:94px;top:55px;width:196px;height:40px;background:#fff;display:flex;align-items:center;gap:6px;padding-left:6px}
.f-brand .dot{width:28px;height:28px;border-radius:50%;background:var(--blue)}
.f-brand span{font-family:"Rubik",sans-serif;font-weight:700;color:var(--blue);font-size:20px}
.f-about{left:94px;top:168px;width:200px;font-size:11px;line-height:17px}
.f-links{left:381px;top:113px;list-style:none;font-size:11px;line-height:26px}
.art{position:absolute;left:570px;width:300px;display:flex;gap:12px;font-family:"Rubik",sans-serif;font-size:11px;line-height:15px}
.art i{width:52px;height:52px;flex:none;background:linear-gradient(135deg,#7fb0e6,#1b3f7a)}
.art b{display:block;font-size:12px;margin-top:4px}
.conn{position:absolute;left:940px;display:flex;gap:14px;font-size:11px;line-height:16px}
.bottom{left:0;top:2901px;width:1200px;height:82px;background:var(--blue);border-top:1px solid rgba(255,255,255,.25);color:#fff;font-family:"Rubik",sans-serif;font-size:12px;text-align:center;padding-top:22px}
</style>
</head>
<body>

<header>
  <div class="abs topbar">
    <div class="abs addr">
      <svg width="12" height="16" viewBox="0 0 12 16"><path d="M6 0a6 6 0 0 0-6 6c0 4.5 6 10 6 10s6-5.5 6-10a6 6 0 0 0-6-6zm0 8.5A2.5 2.5 0 1 1 6 3.5a2.5 2.5 0 0 1 0 5z" fill="#fff"/></svg>
      42 Harbour Lane, Perth, WA 6000
    </div>
    <div class="abs social"><span><i></i></span><span><i></i></span><span><i></i></span></div>
  </div>

  <div class="abs brand">
    <div class="dot"></div>
    <div><div class="name">ST MAREN’S</div><div class="sub">CALVERIN CHURCH PERTH</div></div>
  </div>
  <div class="abs service"><b>WEKEND SERVICE</b>Saturday 6pm<br>Suday 8:30am &amp; 10:20am</div>
</header>

<section>
  <div class="abs hero" role="img" aria-label="Photo of a bright church interior with pews leading to the altar"></div>
  <nav class="abs nav">
    <svg width="1027" height="63" viewBox="0 0 1027 63">
      <path d="M0 12h45v39l-30-4z" fill="var(--blue-dark)"/>
      <path d="M1027 12h-45v39l30-4z" fill="var(--blue-dark)"/>
      <path d="M45 51l20 12v-12z M982 51l-20 12v-12z" fill="#052d5c"/>
      <rect x="40" y="0" width="947" height="51" fill="var(--blue)"/>
    </svg>
    <ul>
      <li class="active">HOME</li><li>SERMONS</li><li>ABOUT US ▾</li><li>CHURCH</li><li>LIFE NEWS</li><li>WEDDINGS</li><li>CONTACT US</li>
    </ul>
  </nav>
  <div class="abs hero-txt">
    <h1>WE Believe that<br>GOD <em>loves Us</em></h1>
    <p>LOVE. GROW. SERVE</p>
  </div>
  <a class="abs btn-touch">GET IN TOUCH</a>
</section>

<section class="abs about"></section>
<svg class="abs notch" width="50" height="28" viewBox="0 0 50 28"><path d="M0 0h50c-8 18-16 26-25 26S8 18 0 0z" fill="#888"/><path d="M17 8l8 7 8-7M17 14l8 7 8-7" stroke="var(--blue)" stroke-width="2" fill="none"/></svg>
<div class="abs notice">
  <div class="ico"><svg width="20" height="18" viewBox="0 0 20 18"><path d="M10 1L19 17H1z" fill="none" stroke="var(--blue)" stroke-width="1.6"/><path d="M10 7v5M10 14v1.5" stroke="var(--blue)" stroke-width="1.6"/></svg></div>
  <h4>St Maren’s response to COVID-19</h4>
  <p>Lorem ipsum dolor sit amet, consectetur adipiscing elit, sed do eiusmod tempor incididunt ut labore et dolore magna aliqua.</p>
</div>
<h2 class="abs h2" style="left:0;top:840px;width:1200px">About Growth Hack</h2>
<div class="abs about-copy">
  <p>Lorem ipsum dolor sit amet, consectetur adipisicing elit, sed do eiusmod tempor incididunt ut labore et dolore magnaaliqua.</p>
  <p>Ut enim ad minim veniam, quis nostrud exercitation ullamco laboris nisi ut aliquip ex ea commodo consequat.</p>
  <p>Duis aute irure dolor in reprehenderit in voluptate velit esse <b>cillum dolore</b> eu fugiat nulla pariatur.</p>
  <p>Excepteur sint occaecat cupidatat non proident, sunt in culpa qui officia deserunt mollit anim id est laborum.<b>voluptatem accusantium</b> doloremque laudantium, totam rem aperiam,</p>
</div>
<div class="abs about-art" role="img" aria-label="Illustration of a church facade framed in decorative shapes with stars"></div>

<section class="abs services">
  <h2 class="h2" style="margin-top:59px">Services We Offer</h2>
</section>
<div class="abs card" style="left:56px;top:1596px"><div class="pic" role="img" aria-label="Photo of an audience listening to a speaker at an event" style="background:linear-gradient(160deg,#6a7fa0,#3a2e2a 60%,#5a3a2c)"><div class="label">ORGANIZED EVENTS</div></div></div>
<div class="abs card" style="left:424px;top:1596px"><div class="pic" role="img" aria-label="Photo of a ring being placed on a hand at a wedding" style="background:linear-gradient(160deg,#c9a28a,#5a3d2e 55%,#2a1e1a)"><div class="label">WEDDINGS</div></div></div>
<div class="abs card" style="left:792px;top:1596px"><div class="pic" role="img" aria-label="Photo of a studio microphone for podcasts and videos" style="background:linear-gradient(160deg,#d8d8d8,#6a6a6a 55%,#b8b2aa)"><div class="label">RECENT PODDCASTS &amp; VIDEOS</div></div></div>

<section class="abs contact" role="img" aria-label="Soft sky background with a cross silhouette"></section>
<svg class="abs ribbon" width="532" height="52" viewBox="0 0 532 52">
  <path d="M0 10h30v40L8 46z M532 10h-30v40l22-4z" fill="var(--blue-dark)"/>
  <rect x="22" y="0" width="488" height="42" fill="var(--blue)"/>
  <text x="253" y="29" text-anchor="middle" font-family="Rubik,sans-serif" font-weight="700" font-size="20" fill="#fff">CONTACT US</text>
</svg>
<div class="abs panel">
  <div class="row" style="top:72px"><span class="c"><svg width="18" height="18" viewBox="0 0 18 18"><path d="M4 1l3 4-2 2c1 2 3 4 5 5l2-2 4 3-2 3C8 16 2 10 1 4z" fill="var(--blue)"/></svg></span>08 9100 4417</div>
  <div class="row" style="top:148px"><span class="c"><svg width="18" height="14" viewBox="0 0 18 14"><rect width="18" height="14" rx="2" fill="var(--blue)"/><path d="M1 2l8 6 8-6" stroke="#fff" fill="none"/></svg></span>hello@stmarens.org.au</div>
  <div class="row" style="top:214px;height:58px"><span class="c"><svg width="18" height="18" viewBox="0 0 18 18"><circle cx="9" cy="9" r="8" fill="none" stroke="var(--blue)" stroke-width="1.6"/><path d="M1 9h16M9 1c-4 5-4 11 0 16M9 1c4 5 4 11 0 16" stroke="var(--blue)" fill="none"/></svg></span>42 Harbour Lane<br>Perth, WA 6000</div>
  <div class="row" style="top:300px"><span class="c"><svg width="18" height="20" viewBox="0 0 18 20"><circle cx="9" cy="11" r="8" fill="none" stroke="var(--blue)" stroke-width="1.6"/><path d="M9 11V6M6 1h6" stroke="var(--blue)" stroke-width="1.6"/></svg></span>Tue,Th&amp; Fri 9.00-4pm</div>
</div>
<a class="abs cta">Contact now</a>
<div class="abs map" role="img" aria-label="Street map showing the church location"></div>

<footer>
  <div class="abs footer">
    <h5 style="left:380px">Quick Links</h5>
    <h5 style="left:570px">Latest Articles</h5>
    <h5 style="left:940px">Let’s Connect</h5>
    <div class="abs f-brand"><div class="dot"></div><span>ST MAREN’S</span></div>
    <div class="abs f-about">Lorem ipsum dolor sit amet, consectetur adipisicing elit, sed do eiusmod tempor incididunt ut labore et dolore magna aliqua. Ut enim ad minim veniam, quis nostrud.</div>
    <ul class="abs f-links"><li>Home</li><li>Sernons</li><li>About Us</li><li>Contact Us</li><li>News</li><li>Weddings</li><li>Sitemap</li></ul>
    <div class="art" style="top:112px"><i role="img" aria-label="Article thumbnail"></i><div>Lorem ipsum dolor sit amet, conse cterud , cons ectetur, adipis ci velit, sed<b>1 Dec, 2020</b></div></div>
    <div class="art" style="top:189px"><i role="img" aria-label="Article thumbnail"></i><div>Lorem ipsum dolor sit amet, conse cterud , cons ectetur, adipis ci velit, sed<b>1 Dec, 2020</b></div></div>
    <div class="art" style="top:270px"><i role="img" aria-label="Article thumbnail"></i><div>Lorem ipsum dolor sit amet, conse cterud , cons ectetur, adipis ci velit, sed<b>1 Dec, 2020</b></div></div>
    <div class="conn" style="top:113px;left:938px"><svg width="20" height="18" viewBox="0 0 18 18"><path d="M4 1l3 4-2 2c1 2 3 4 5 5l2-2 4 3-2 3C8 16 2 10 1 4z" fill="var(--gold)"/></svg>08 9100 4417</div>
    <div class="conn" style="top:150px;left:942px"><svg width="14" height="18" viewBox="0 0 12 16"><path d="M6 0a6 6 0 0 0-6 6c0 4.5 6 10 6 10s6-5.5 6-10a6 6 0 0 0-6-6zm0 8.5A2.5 2.5 0 1 1 6 3.5a2.5 2.5 0 0 1 0 5z" fill="var(--gold)"/></svg><span style="margin-left:4px">42 Harbour Lane<br>Perth,,WA 6000</span></div>
    <div class="conn" style="top:203px;left:938px"><svg width="20" height="16" viewBox="0 0 20 16"><path d="M0 8L20 0 15 16 10 10z" fill="var(--gold)"/></svg>hello@stmarens.org.au</div>
  </div>
  <div class="abs bottom">© 2020 St Maren’s Church&nbsp; LLC.</div>
</footer>

</body>
</html>
```